Dental Specialist Needs a Business Card

We are a state of the art dental specialty office and need a business card that looks modern but professional.
I have provided our logo design in both vertical and horizontal. We use the design on letterhead in the vertical format but provided both forms for you. Thanks
Updates

Please add the address, phone and fax numbers I listed to all designs and please leave a space for website and for my employee name on each design. Thanks 2847 Marlow Avenue, Suite K East Brantham, NY 14391 Phone (716)392-5174 Fax:(716)392-5179 My name is Devin R.Holloway,D.D.S. If you want to show it with my name but the design needs to allow for the name to be switched.

Industry/Entity Type

Business

```html
<!DOCTYPE html>
<html lang="en">
<head>
<meta charset="utf-8">
<title>Keystone Endodontics P.C. — Business Card</title>
<link href="https://fonts.googleapis.com/css2?family=Open+Sans:wght@400;600;700&display=swap" rel="stylesheet">
<style>
  :root {
    --stage: #3a3a3a;
    --card-dark: #050505;
    --card-light: #fbfbfb;
    --brand-blue: #1f8fd8;
    --brand-green: #7dc242;
    --deco-green: rgba(34, 110, 40, 0.55);
    --deco-blue: rgba(28, 80, 112, 0.55);
    --ink: #2b2b2b;
    --ink-soft: #555555;
    --rule: #b9b9b9;
    --white: #ffffff;
  }
  * { margin: 0; padding: 0; box-sizing: border-box; }
  html, body { width: 1200px; height: 720px; overflow: hidden; }
  body {
    background: var(--stage);
    font-family: "Open Sans", Arial, sans-serif;
    position: relative;
  }
  .card {
    position: absolute;
    top: 210px;
    width: 525px;
    height: 300px;
    border-radius: 16px;
    overflow: hidden;
  }
  .card--back { left: 50px; background: var(--card-dark); }
  .card--front { left: 625px; background: var(--card-light); color: var(--ink); }

  .back-decoration {
    position: absolute; left: 150px; top: 0; right: 0; height: 250px;
    background:
      radial-gradient(ellipse 45% 40% at 88% 30%, var(--deco-blue), transparent 70%),
      radial-gradient(ellipse 60% 55% at 45% 45%, var(--deco-green), transparent 72%);
  }
  .back-brand {
    position: absolute; left: 40px; bottom: 48px;
    display: flex; align-items: center; gap: 12px;
    color: var(--white); font-weight: 700;
  }
  .brand-dot { width: 22px; height: 22px; border-radius: 50%; background: var(--brand-blue); flex: none; }
  .brand-name { font-size: 24px; line-height: 1.1; letter-spacing: 0.5px; }
  .brand-name span { display: block; font-size: 13px; letter-spacing: 1px; }

  .front-brand {
    position: absolute; left: 30px; top: 56px;
    display: flex; align-items: center; gap: 12px;
    font-weight: 700; color: var(--ink);
  }

  .holder { position: absolute; right: 30px; top: 24px; text-align: right; color: var(--ink-soft); }
  .holder-name { font-size: 11px; letter-spacing: 1px; text-transform: uppercase; }
  .holder-title { font-size: 8px; letter-spacing: 1px; }

  .stripes { position: absolute; inset: 0; width: 100%; height: 100%; }

  .rule-dashed { position: absolute; height: 0; border-top: 1px dashed var(--rule); }
  .rule-top { left: 300px; right: 24px; top: 100px; }
  .rule-mid { left: 24px; right: 200px; top: 212px; }

  .contact { position: absolute; display: flex; align-items: center; gap: 10px; font-size: 12px; color: var(--ink); white-space: nowrap; }
  .contact svg { width: 14px; height: 14px; fill: #333; flex: none; }
  .contact--address { left: 28px; top: 186px; font-size: 11.5px; }
  .contact--email { left: 28px; top: 226px; }
  .contact--web { left: 28px; top: 252px; }
  .contact--phone { right: 30px; top: 150px; }
  .contact--fax { right: 30px; top: 174px; }
</style>
</head>
<body>

<section class="card card--back" aria-label="Card back">
  <div class="back-decoration" role="img" aria-label="Soft green and blue brand swoosh decoration"></div>
  <div class="back-brand">
    <div class="brand-dot"></div>
    <div class="brand-name">KEYSTONE<span>Endodontics P.C.</span></div>
  </div>
</section>

<section class="card card--front" aria-label="Card front">
  <div class="front-brand">
    <div class="brand-dot"></div>
    <div class="brand-name">KEYSTONE<span>Endodontics P.C.</span></div>
  </div>

  <div class="holder">
    <div class="holder-name">Devin R.Holloway</div>
    <div class="holder-title">D.D.S.</div>
  </div>

  <div class="rule-dashed rule-top"></div>

  <svg class="stripes" viewBox="0 0 525 300" aria-hidden="true">
    <polygon points="0,150 525,112 525,120 0,158" fill="var(--brand-blue)"/>
    <polygon points="0,166 525,128 525,136 0,174" fill="var(--brand-green)"/>
  </svg>

  <div class="contact contact--address">
    <svg viewBox="0 0 24 24" aria-hidden="true"><path d="M12 2a7 7 0 0 0-7 7c0 5 7 13 7 13s7-8 7-13a7 7 0 0 0-7-7zm0 9.5A2.5 2.5 0 1 1 12 6.5a2.5 2.5 0 0 1 0 5z"/></svg>
    <span>2847 Marlow Avenue, Suite K East Brantham, NY 14391</span>
  </div>
  <div class="rule-dashed rule-mid"></div>
  <div class="contact contact--email">
    <svg viewBox="0 0 24 24" aria-hidden="true"><path d="M2 5h20v14H2zM4 7v.5l8 5 8-5V7l-8 5z"/></svg>
    <span>Email@youremail.com</span>
  </div>
  <div class="contact contact--web">
    <svg viewBox="0 0 24 24" aria-hidden="true"><path d="M2 4h20v13H2zm2 2v9h16V6zM8 19h8v2H8z"/></svg>
    <span>http://www.yourwebsite.com</span>
  </div>

  <div class="contact contact--phone">
    <svg viewBox="0 0 24 24" aria-hidden="true"><path d="M6.6 10.8a15 15 0 0 0 6.6 6.6l2.2-2.2a1 1 0 0 1 1-.25 11.4 11.4 0 0 0 3.6.6 1 1 0 0 1 1 1V20a1 1 0 0 1-1 1A17 17 0 0 1 3 4a1 1 0 0 1 1-1h3.5a1 1 0 0 1 1 1c0 1.25.2 2.45.6 3.6a1 1 0 0 1-.25 1z"/></svg>
    <span>(716)392-5174</span>
  </div>
  <div class="contact contact--fax">
    <svg viewBox="0 0 24 24" aria-hidden="true"><path d="M7 3h10v5H7zM4 9h16a2 2 0 0 1 2 2v6h-4v4H6v-4H2v-6a2 2 0 0 1 2-2zm4 7v3h8v-3z"/></svg>
    <span>(716)392-5179</span>
  </div>
</section>

</body>
</html>
```